Banner 34"x81"

This is for a Pull Up Banner
I am supplying a sample of my logo and some of my art work for you to incorporate into an upright banner.
Please business name:LuellaRo OpenHarbor Psychotherapy
phone number: 583-214-9067 NOT THE ONE ON THE BUSINESS CARD

```html
<!DOCTYPE html>
<html lang="en">
<head>
<meta charset="utf-8">
<title>LuellaRo OpenHarbor Psychotherapy – Pull Up Banner</title>
<link href="https://fonts.googleapis.com/css2?family=Exo+2:wght@300;400;600&family=Archivo+Black&display=swap" rel="stylesheet">
<style>
  :root {
    --page-bg: #e9e7e4;
    --navy-deep: #050a1e;
    --navy: #0d1a4a;
    --royal: #1a3fa0;
    --glow: #2466c4;
    --gold: #d2b45a;
    --white: #f4f4f6;
    --frame-red: #e0141c;
    --logo-blue: #2456a8;
  }
  * { margin: 0; padding: 0; box-sizing: border-box; }
  html, body { width: 1200px; height: 1200px; overflow: hidden; background: var(--page-bg); }
  .banner {
    position: absolute; left: 366px; top: 28px; width: 468px; height: 1144px; overflow: hidden;
    background:
      radial-gradient(ellipse 55% 45% at 10% 48%, rgba(36,102,196,.75), transparent 70%),
      radial-gradient(ellipse 70% 40% at 45% 22%, rgba(26,63,160,.8), transparent 75%),
      linear-gradient(180deg, var(--navy-deep) 0%, var(--navy) 12%, var(--navy) 70%, var(--navy-deep) 100%);
    font-family: "Exo 2", sans-serif;
  }
  .brand-mark {
    position: absolute; left: 183px; top: 59px; width: 105px; height: 87px;
    background: var(--logo-blue); color: var(--white);
    display: flex; align-items: center; justify-content: center;
    font-family: "Exo 2", sans-serif; font-weight: 400; font-size: 48px; letter-spacing: 2px;
  }
  .business-name {
    position: absolute; left: 0; width: 100%; text-align: center;
    color: var(--gold); font-weight: 300; font-size: 60px; line-height: 56px; letter-spacing: 5px;
  }
  .business-name.line-1 { top: 178px; }
  .business-name.line-2 { top: 234px; }
  .practice-type {
    position: absolute; top: 292px; left: 0; width: 100%; text-align: center;
    color: var(--white); font-weight: 300; font-size: 28px; letter-spacing: 3px;
  }
  .portrait-frame {
    position: absolute; left: 58px; top: 360px; width: 362px; height: 560px;
    border: 5px solid var(--frame-red);
  }
  .frame-base {
    position: absolute; left: 58px; top: 915px; width: 410px; height: 5px; background: var(--frame-red);
  }
  .portrait {
    position: absolute; left: 176px; top: 388px; width: 292px; height: 525px;
    background:
      radial-gradient(ellipse 40% 28% at 50% 22%, #1c1c24 0%, transparent 80%),
      radial-gradient(ellipse 55% 30% at 52% 62%, #2e55b8 0%, transparent 80%),
      radial-gradient(ellipse 50% 22% at 55% 92%, #8a8c96 0%, transparent 85%);
  }
  .vertical-name { position: absolute; left: 84px; top: 378px; width: 66px; height: 516px; }
  .vertical-name text {
    font-family: "Archivo Black", sans-serif; font-size: 64px;
    fill: none; stroke: var(--gold); stroke-width: 1.2;
  }
  .phone {
    position: absolute; top: 942px; left: 0; width: 100%; text-align: center;
    color: var(--gold); font-weight: 600; font-size: 56px; letter-spacing: 0;
  }
  .contact-row {
    position: absolute; top: 1013px; left: 56px; width: 380px;
    display: flex; justify-content: space-between; align-items: center;
    color: var(--white); font-size: 8.5px; font-weight: 400;
  }
  .contact-item { display: flex; align-items: center; gap: 3px; }
  .contact-icon { width: 11px; height: 11px; border-radius: 50%; background: var(--gold); display: inline-block; }
  .contact-icon svg { display: block; }
</style>
</head>
<body>
  <main class="banner">
    <div class="brand-mark">LR</div>
    <h1 class="business-name line-1">OPEN</h1>
    <h1 class="business-name line-2">HARBOR</h1>
    <p class="practice-type">PSYCHOTHERAPY</p>

    <div class="portrait-frame"></div>
    <div class="frame-base"></div>
    <div class="portrait" role="img" aria-label="Portrait of the therapist in a blue top, seated and smiling"></div>

    <svg class="vertical-name" viewBox="0 0 66 516" aria-label="LUELLARO">
      <text transform="translate(60 512) rotate(-90)" textLength="508" lengthAdjust="spacingAndGlyphs">LUELLARO</text>
    </svg>

    <p class="phone">583-214-9067</p>

    <div class="contact-row">
      <span class="contact-item">
        <span class="contact-icon">
          <svg width="11" height="11" viewBox="0 0 11 11"><rect x="2.5" y="3.5" width="6" height="4" fill="none" stroke="#0d1a4a" stroke-width=".8"/><path d="M2.5 3.5 5.5 6 8.5 3.5" fill="none" stroke="#0d1a4a" stroke-width=".8"/></svg>
        </span>LuellaOpenHarbor@mail.com
      </span>
      <span class="contact-item"><span class="contact-icon"></span>@LuellaOpenHarbor</span>
      <span class="contact-item"><span class="contact-icon"></span>@LuellaHarbor</span>
    </div>
  </main>
</body>
</html>
```